I want a business card that is going to show a creative spark but without limiting me to an industry. Something edgy but that wont go out of date. I want it state My business name Verity Lanes, profession - Professional Makeup Artist contact number and email

My service is to provide makeup services from bridal, fashion, photography, film, TV and so on. It is creative and different so i want that to be reflected.

I would like the card double sided.
Updates

 I would LOVE a background on my card something like this image... i can supply an image to be formed like this

Please use the image uploaded

Can we try using the image provided on one side of the card and then writing and details on the other side

Target Market(s)

I am targeting a wide range of people from Creative directors to the individual eg. bride

Industry/Entity Type

Business

Requirements
Must have
• Name: Harriet Cole
contact numbe 0417 583 940
email address:info@veritylanes.example
website: www.veritylanes.example
One of the images attached

professional makeup artist / hair stylist

I want it to show creativity
Nice to have
• logo, Double-sided card
Should not have
• the design should not use tradional style. Or images that are not my own

```html
<!DOCTYPE html>
<html lang="en">
<head>
<meta charset="utf-8">
<title>Verity Lanes — Identity and Business Card</title>
<link rel="stylesheet" href="https://fonts.googleapis.com/css2?family=Mulish:wght@300;400&family=Roboto+Condensed:wght@300&display=swap">
<style>
  :root {
    --paper: #ffffff;
    --mark-grey: #a7a8aa;
    --ink: #231f20;
    --card-black: #000000;
    --card-strip: #1c1c1c;
    --card-grey: #808083;
    --soft-white: #e6e6e6;
    --muted: #b9b9bb;
    --back-text: #f2f2f2;
    --back-muted: #c4c4c6;
    --photo-dark: #1e1e1e;
    --photo-light: #8a8a8a;
  }
  * { margin: 0; padding: 0; box-sizing: border-box; }
  html, body { width: 1200px; height: 1200px; overflow: hidden; background: var(--paper); }
  .board { position: relative; width: 1200px; height: 1200px; background: var(--paper); font-family: "Mulish", sans-serif; }

  /* Identity lockup */
  .identity-square { position: absolute; left: 527px; top: 190px; width: 146px; height: 146px; background: var(--mark-grey); }
  .identity-name {
    position: absolute; left: 0; width: 1200px; top: 400px; text-align: center;
    font-weight: 300; font-size: 27px; letter-spacing: 0.42em; padding-left: 0.42em; color: var(--ink);
  }

  /* Cards */
  .card { position: absolute; overflow: hidden; }

  .card-front { left: 147px; top: 581px; width: 490px; height: 259px; background: var(--card-black); box-shadow: 4px 6px 10px rgba(0,0,0,0.18); }
  .front-square { position: absolute; left: 138px; top: 94px; width: 26px; height: 26px; background: var(--mark-grey); }
  .front-name {
    position: absolute; left: 0; width: 291px; top: 155px; text-align: center;
    font-weight: 400; font-size: 11px; letter-spacing: 0.36em; padding-left: 0.36em; color: var(--soft-white);
  }
  .front-web {
    position: absolute; left: 0; width: 284px; top: 229px; text-align: right;
    font-family: "Roboto Condensed", sans-serif; font-weight: 300; font-size: 12px; color: var(--muted);
  }
  .portrait {
    position: absolute; left: 291px; top: 0; width: 173px; height: 259px;
    background: linear-gradient(160deg, var(--photo-dark) 0%, var(--photo-light) 45%, #5a5a5a 70%, var(--photo-dark) 100%);
  }
  .edge-strip { position: absolute; left: 464px; top: 0; width: 26px; height: 259px; background: var(--card-strip); }

  .card-back { left: 572px; top: 789px; width: 490px; height: 259px; background: var(--card-grey); box-shadow: 6px 8px 12px rgba(0,0,0,0.2); }
  .back-name { position: absolute; left: 42px; top: 71px; font-weight: 400; font-size: 13px; color: var(--back-text); }
  .back-role {
    position: absolute; left: 42px; top: 93px; font-weight: 400; font-size: 8.5px;
    letter-spacing: 0.04em; text-transform: uppercase; color: var(--back-muted);
  }
  .contact { position: absolute; left: 42px; top: 147px; list-style: none; font-weight: 400; font-size: 11.5px; color: var(--back-text); }
  .contact li { display: flex; align-items: center; height: 23px; }
  .contact .label { width: 14px; font-size: 6px; color: var(--back-muted); }
  .back-square { position: absolute; right: 0; bottom: 0; width: 150px; height: 100px; background: var(--paper); }
</style>
</head>
<body>
<main class="board">
  <div class="identity-square" aria-hidden="true"></div>
  <p class="identity-name">VERITY LANES</p>

  <section class="card card-front" aria-label="Business card front">
    <div class="front-square" aria-hidden="true"></div>
    <p class="front-name">VERITY LANES</p>
    <p class="front-web">veritylanes.example</p>
    <div class="portrait" role="img" aria-label="Black and white portrait photograph of a model with long wavy hair"></div>
    <div class="edge-strip" aria-hidden="true"></div>
  </section>

  <section class="card card-back" aria-label="Business card back">
    <p class="back-name">Harriet Cole</p>
    <p class="back-role">Professional Make Up Artist / Hair Stylist</p>
    <ul class="contact">
      <li><span class="label">t</span>0417 583 940</li>
      <li><span class="label">e</span>info@veritylanes.example</li>
    </ul>
    <div class="back-square" aria-hidden="true"></div>
  </section>
</main>
</body>
</html>
```